New PowerPoint Design Project

A well-known speaker needs a visual presence that compliments his amazing, consistent performance onstage. You'll easily improve this deck, and I'll leave it to you whether you stick with the palette defined by the original PLMVUE icons you'll find in the deck, the mishmosh in the deck as it stands, OR get extra points by going with the corporate color palette so our speaking slides fit with Marlon's brands and his three sub-brands. A look at the Marlon subbrand .png in the attached zip file might give you some ideas.
Updates

Just noting that I'm available to answer questions or supply assets you think you'd need. The big design issue I'm looking for someone to solve is how you'll treat the bright clusters of icons in information graphics of the deck.

Target Market(s)

Corporate Executives and wanabees

Requirements
Must have
• The footer needs to have the Dunwoody Sparkpath logo and Twitter and Facebook link and you need to do the first 27 slides. The slides past 27 are there simply if you want to use assets from those slides.
Nice to have
• Use the palette document in the zip rather than palette dictated by the PLMVUE icons in the deck (I do not have source for the icons.).

```html
<!DOCTYPE html>
<html lang="en">
<head>
<meta charset="utf-8">
<title>Mission 7 – Lead with Generosity</title>
<link rel="stylesheet" href="https://fonts.googleapis.com/css2?family=Arimo:wght@400;700&display=swap">
<style>
  :root {
    --bg: #ffffff;
    --ink-dark: #222222;
    --teal: #4c7f8e;
    --teal-deep: #3f6f7d;
    --orange: #e27b1c;
    --tab: #3a3a3a;
    --footer: #2f2f2f;
    --footer-text: #d9d9d9;
    --muted: #8a8a8a;
    --icon-border: #9aa4a8;
    --photo-light: #f3ede6;
    --photo-mid: #dcc3a6;
  }
  * { margin: 0; padding: 0; box-sizing: border-box; }
  html, body { width: 1200px; height: 675px; overflow: hidden; background: var(--bg); }
  body { font-family: "Arimo", Arial, sans-serif; }

  .slide { position: relative; width: 1200px; height: 675px; background: var(--bg); overflow: hidden; }

  .mission-label {
    position: absolute; left: 33px; top: 30px;
    font-size: 28px; font-weight: 700; line-height: 34px; color: var(--ink-dark);
  }
  .mission-title {
    position: absolute; left: 33px; top: 70px;
    font-size: 54px; font-weight: 700; line-height: 69px;
    color: var(--teal); letter-spacing: 3.5px; text-transform: uppercase;
  }

  .coffee-photo {
    position: absolute; left: 735px; top: 80px; width: 465px; height: 500px;
    background: linear-gradient(160deg, var(--photo-light) 0%, var(--photo-mid) 55%, var(--photo-light) 100%);
  }

  .mission-tab {
    position: absolute; left: 30px; top: 447px; width: 38px; height: 145px;
    background: var(--tab);
    display: flex; align-items: center; justify-content: center;
  }
  .mission-tab span {
    transform: rotate(-90deg); white-space: nowrap;
    color: #ffffff; font-size: 26px; font-weight: 700;
  }

  .mission-task {
    position: absolute; left: 130px; top: 453px;
    font-size: 37px; font-weight: 700; line-height: 44px;
    letter-spacing: 1px; color: var(--teal-deep);
  }
  .mission-task .accent { color: var(--orange); }

  .outreach-icon {
    position: absolute; left: 626px; top: 442px; width: 157px; height: 145px;
    border: 2px solid var(--icon-border); border-radius: 10px; background: #fff;
    display: flex; flex-direction: column; align-items: center; padding: 8px;
  }
  .outreach-icon .art {
    width: 137px; height: 98px; border-radius: 4px;
    background: linear-gradient(180deg, #c7d9a9 0%, #7fa9b3 60%, #4e6e7a 100%);
  }
  .outreach-icon .caption {
    margin-top: 9px; font-size: 15px; letter-spacing: 3px; color: #555;
  }

  .footer {
    position: absolute; left: 0; top: 627px; width: 1200px; height: 48px;
    background: var(--footer); color: var(--footer-text);
  }
  .brand {
    position: absolute; left: 28px; top: 0; height: 48px;
    display: flex; align-items: center; gap: 10px; font-size: 22px;
  }
  .brand .mark { width: 24px; height: 24px; background: var(--footer-text); }
  .social {
    position: absolute; top: 0; height: 48px;
    display: flex; align-items: center; gap: 8px; font-size: 13px;
  }
  .social.facebook { left: 842px; }
  .social.twitter { left: 992px; }
  .social .mark { width: 26px; height: 26px; background: #5b7fbf; border-radius: 3px; }
  .social.twitter .mark { background: #5fb2dd; }
  .page-number {
    position: absolute; left: 1160px; top: 0; line-height: 48px;
    color: var(--muted); font-size: 13px;
  }
</style>
</head>
<body>
  <main class="slide">
    <p class="mission-label">Mission 7:</p>
    <h1 class="mission-title">Lead with<br>generosity,<br>intimacy, candor<br>and accountability</h1>

    <div class="coffee-photo" role="img" aria-label="Photo of two cappuccino cups with cocoa-dusted foam on white saucers"></div>

    <div class="mission-tab"><span>Mission</span></div>
    <p class="mission-task">
      <span class="accent">Ping with gratitude and<br>respect.</span> Ask for COFFEE,<br>LUNCH, a CALL
    </p>

    <div class="outreach-icon">
      <div class="art" role="img" aria-label="Icon of a person reaching out to a network of contacts"></div>
      <span class="caption">OUTREACH</span>
    </div>

    <footer class="footer">
      <div class="brand"><span class="mark"></span>Dunwoody Sparkpath</div>
      <div class="social facebook"><span class="mark"></span><span>/MarlonDunwoody</span></div>
      <div class="social twitter"><span class="mark"></span><span>@dunwoody</span></div>
      <span class="page-number">27</span>
    </footer>
  </main>
</body>
</html>
```